QR-482 Horizons, LLC business cards
Personal Fitness Training
Professional
QR 482 Horizons, LLC
Fitness Solutions
based out of Miami but want to train internationally over the net
bellamorvain@qr482.net
www.qr482.net
K20000047153
I would also like to list my bellamorvain@zentmail.net email
I will be based out of the Miami area but do not have an exact location for the address.
Contact for your Free Fitness Assessment
415 263 9071 or bellamorvain@qr482.net

```html
<!DOCTYPE html>
<html lang="en">
<head>
<meta charset="utf-8">
<title>QR-482 Horizons, LLC Stationery</title>
<link rel="stylesheet" href="https://fonts.googleapis.com/css2?family=Open+Sans:ital,wght@0,400;0,700;1,400&display=swap">
<style>
  :root {
    --blue: #2a9ad8;
    --blue-light: #5cc0ef;
    --grey: #a9adb2;
    --grey-dark: #6f747a;
    --ink: #3d4147;
    --paper: #ffffff;
    --bg: #ffffff;
    --shadow: rgba(0,0,0,0.28);
  }
  html, body { margin: 0; padding: 0; overflow: hidden; }
  body {
    width: 1200px; height: 681px; position: relative;
    background: var(--bg);
    font-family: "Open Sans", Arial, sans-serif;
    color: var(--ink);
  }
  .sheet {
    position: absolute; background: var(--paper);
    box-shadow: 2px 3px 8px var(--shadow);
    overflow: hidden;
  }
  .band { position: absolute; left: 0; top: 0; width: 100%; display: block; }
  .brand {
    position: absolute; display: flex; align-items: center; gap: 6px;
    transform: translate(-50%, -50%);
    font-weight: 700; color: var(--grey-dark); white-space: nowrap;
  }
  .brand-mark { background: var(--blue); display: block; }
  .envelope-front { left: 53px; top: 96px; width: 475px; height: 216px; }
  .envelope-front .brand { left: 50%; top: 88px; font-size: 30px; }
  .envelope-front .brand-mark { width: 22px; height: 22px; }
  .envelope-back { left: 53px; top: 348px; width: 475px; height: 240px; }
  .flap { position: absolute; left: 0; top: 0; width: 100%; height: 100%; }
  .envelope-back .brand-mark {
    position: absolute; left: 50%; top: 68px; width: 28px; height: 28px;
    transform: translate(-50%, -50%);
  }
  .letterhead { left: 617px; top: 36px; width: 331px; height: 600px; }
  .letterhead .brand { left: 50%; top: 96px; font-size: 26px; }
  .letterhead .brand-mark { width: 18px; height: 18px; }
  .letterhead-contact {
    position: absolute; left: 0; right: 0; top: 178px;
    text-align: center; font-size: 7px; color: var(--grey-dark);
  }
  .card { width: 161px; height: 113px; left: 967px; }
  .card-front { top: 175px; }
  .card-back { top: 312px; }
  .card-front .brand { left: 50%; top: 34px; font-size: 15px; }
  .card-front .brand-mark { width: 10px; height: 10px; }
  .card-role { position: absolute; left: 0; right: 0; top: 58px; text-align: center; font-size: 5px; color: var(--grey-dark); }
  .card-name {
    position: absolute; left: 0; right: 0; top: 84px; text-align: center;
    font-size: 6px; color: var(--blue); line-height: 1.4;
  }
  .card-name strong { display: block; font-weight: 700; }
  .card-back .brand-mark {
    position: absolute; left: 50%; top: 22px; width: 14px; height: 14px;
    transform: translate(-50%, -50%);
  }
  .card-details {
    position: absolute; left: 0; right: 0; top: 52px; text-align: center;
    font-size: 5px; line-height: 1.55; color: var(--ink);
  }
</style>
</head>
<body>

<section class="sheet envelope-front">
  <svg class="band" viewBox="0 0 475 90" height="90" preserveAspectRatio="none" aria-hidden="true">
    <path d="M0 0H475V66Q237 2 0 66Z" fill="var(--blue)"/>
    <path d="M0 66Q237 2 475 66V78Q237 16 0 78Z" fill="var(--grey)"/>
  </svg>
  <div class="brand"><span class="brand-mark"></span>QR-482</div>
</section>

<section class="sheet envelope-back">
  <svg class="flap" viewBox="0 0 475 240" preserveAspectRatio="none" aria-hidden="true">
    <path d="M2 6Q10 4 20 30L50 92Q54 100 64 100H411Q421 100 425 92L455 30Q465 4 473 6" fill="none" stroke="var(--grey-dark)" stroke-width="1"/>
  </svg>
  <span class="brand-mark"></span>
</section>

<section class="sheet letterhead">
  <svg class="band" viewBox="0 0 331 100" height="100" preserveAspectRatio="none" aria-hidden="true">
    <path d="M0 0H331V82Q165 30 0 82Z" fill="var(--blue)"/>
    <path d="M0 82Q165 30 331 82V92Q165 42 0 92Z" fill="var(--grey)"/>
  </svg>
  <div class="brand"><span class="brand-mark"></span>QR-482</div>
  <p class="letterhead-contact">415 263 9071 &nbsp;•&nbsp; www.qr482.net</p>
</section>

<section class="sheet card card-front">
  <svg class="band" viewBox="0 0 161 40" height="40" preserveAspectRatio="none" aria-hidden="true">
    <path d="M0 0H161V30Q80 8 0 30Z" fill="var(--blue)"/>
    <path d="M0 30Q80 8 161 30V35Q80 14 0 35Z" fill="var(--grey)"/>
  </svg>
  <div class="brand"><span class="brand-mark"></span>QR-482</div>
  <p class="card-role">Personal Trainer</p>
  <p class="card-name"><strong>Bella Morvain</strong>bellamorvain@qr482.net</p>
</section>

<section class="sheet card card-back">
  <span class="brand-mark"></span>
  <p class="card-details">
    Contact for your Free Fitness Assessment<br>
    415 263 9071<br>
    bellamorvain@zentmail.net<br>
    www.qr482.net
  </p>
</section>

</body>
</html>
```